Beacon Advisory Website

I currently have a website www.beaconadvisoryinc.example. We are a IT Consulting Company. Our website will pretty much tell out our services. I am looking to enhance my website and make it look more professional. Looking for very classy and Contemporary look and design for my website.

Industry/Entity Type

It Company

```html
<!DOCTYPE html>
<html lang="en">
<head>
<meta charset="utf-8">
<title>Beacon Advisory</title>
<link href="https://fonts.googleapis.com/css2?family=Lato:wght@400;700&family=Oswald:wght@400&family=Questrial&display=swap" rel="stylesheet">
<style>
:root{
  --navy:#0e3a86;
  --navy-dark:#0b2f70;
  --ink:#222;
  --footer:#2a2a2a;
  --footer-line:#3c3c3c;
  --card:#1d1f22;
  --white:#fff;
}
*{box-sizing:border-box;margin:0;padding:0}
html,body{width:1010px;height:1200px;overflow:hidden;background:#fff}
body{position:relative;font-family:"Lato",sans-serif;color:var(--ink)}
.topbar{position:absolute;left:0;top:0;width:1010px;height:27px;background:var(--navy)}
.topbar .phone{position:absolute;right:220px;top:6px;color:#fff;font:700 13px "Lato",sans-serif;display:flex;align-items:center;gap:6px}
.topbar .social{position:absolute;right:83px;top:0;display:flex}
.topbar .social span{width:29px;height:27px;background:var(--navy-dark);border-left:1px solid rgba(255,255,255,.25);display:flex;align-items:center;justify-content:center}
.topbar .social span i{width:11px;height:11px;border:1.5px solid #fff;border-radius:50%;display:block}
.header{position:absolute;top:27px;left:0;width:1010px;height:70px;background:#fff;border-bottom:1px solid #cfd6df}
.brand{position:absolute;left:84px;top:20px;display:flex;align-items:center;gap:8px}
.brand .mark{width:26px;height:26px;background:var(--navy);border-radius:3px}
.brand .name{font:700 21px "Lato",sans-serif;color:var(--navy);letter-spacing:.5px}
.nav{position:absolute;right:85px;top:24px;display:flex;align-items:center;font:14px "Questrial",sans-serif;color:#333}
.nav a{color:#333;text-decoration:none;padding:0 9px;border-left:1px solid #ccc;line-height:16px}
.nav .home{border:none;padding-right:13px}
.hero{position:absolute;top:98px;left:0;width:1010px;height:540px;background:linear-gradient(100deg,#8fb0c6 0%,#b9d3e2 40%,#cfe3ee 65%,#a9c4d4 100%)}
.hero h1{position:absolute;left:84px;top:108px;font:400 25px/30px "Oswald",sans-serif;color:#fff;text-shadow:0 1px 3px rgba(0,0,0,.5);letter-spacing:.2px}
.cta{position:absolute;left:84px;top:220px;width:209px;height:43px;background:var(--navy);border:2px solid #fff;color:#fff;font:700 17px/39px "Lato",sans-serif;text-align:center}
.card{position:absolute;top:348px;width:255px;height:151px;background:var(--card);border-radius:3px;box-shadow:0 6px 8px rgba(0,0,0,.25)}
.card .tab{position:absolute;left:-4px;top:5px;width:230px;height:32px;background:#fff;clip-path:polygon(0 0,100% 0,92% 100%,0 100%);font:15px/32px "Questrial",sans-serif;color:var(--navy);padding-left:15px;letter-spacing:.3px}
.card .icon{position:absolute;left:16px;top:51px;width:65px;height:65px;border-radius:50%;background:var(--navy);border:2px solid #fff;display:flex;align-items:center;justify-content:center}
.card p{position:absolute;left:95px;top:51px;width:150px;font:10px/14px "Lato",sans-serif;color:#eee}
.card .more{position:absolute;right:22px;bottom:11px;font:10.5px "Lato",sans-serif;color:#eee;text-decoration:underline}
.welcome{position:absolute;top:670px;left:0;width:1010px;text-align:center}
.welcome h2{font:400 23px "Questrial",sans-serif;color:#222;display:inline-flex;align-items:center;gap:10px}
.welcome h2 .dot{width:22px;height:22px;border-radius:50%;background:var(--navy)}
.welcome h2 strong{color:var(--navy);font-weight:700;font-family:"Lato",sans-serif}
.rule{position:absolute;top:711px;left:224px;width:562px;border-top:1px dotted #999}
.points{position:absolute;top:733px;left:84px;width:470px;list-style:none}
.points li{position:relative;padding-left:28px;font:12px/16px "Lato",sans-serif;color:#333;margin-bottom:12px}
.points svg{position:absolute;left:0;top:3px}
.tablet{position:absolute;left:590px;top:735px;width:336px;height:224px;background:linear-gradient(180deg,#e9d0c0,#d6b19a)}
.footer{position:absolute;top:959px;left:0;width:1010px;height:205px;background:var(--footer)}
.col h3{font:700 15px "Lato",sans-serif;color:#fff;letter-spacing:.5px;padding-bottom:8px;border-bottom:1px solid var(--footer-line);margin-bottom:8px}
.col{position:absolute;top:22px;color:#ddd;font:11.5px "Lato",sans-serif}
.links{left:86px;width:108px}
.links li{list-style:none;line-height:19.5px}
.links li::before{content:"»";color:#aaa;margin-right:12px;font-size:12px}
.contact{left:266px;width:164px}
.contact .row{display:flex;gap:8px;margin-bottom:12px;line-height:15px}
.contact .row svg{flex-shrink:0;margin-top:2px}
.inquiry{left:503px;width:190px}
.inquiry .field{width:183px;height:22px;background:#fff;border:1px solid #ccc;margin-bottom:7px;color:#666;font-size:10px;padding:4px 6px}
.inquiry .msg{height:36px}
.inquiry .btn{width:54px;height:21px;background:var(--navy);color:#fff;font:700 11px/21px "Lato",sans-serif;text-align:center;margin-top:1px}
.sep{position:absolute;top:60px;width:1px;height:110px;background:#3a3a3a}
.f-brand{position:absolute;left:770px;top:83px;display:flex;align-items:center;gap:8px}
.f-brand .mark{width:24px;height:24px;border-radius:3px;background:#888}
.f-brand .name{font:700 19px "Lato",sans-serif;color:#bbb}
.f-social{position:absolute;left:784px;top:133px;display:flex;gap:7px}
.f-social span{width:25px;height:25px;border-radius:50%}
.copy{position:absolute;top:1164px;left:0;width:1010px;height:36px;background:var(--navy);color:#fff;font:11px/36px "Lato",sans-serif;text-align:center}
</style>
</head>
<body>
<div class="topbar">
  <div class="phone"><svg width="12" height="13" viewBox="0 0 12 13"><path d="M3 1l2 3-1.5 1.5c.7 1.6 2 2.9 3.5 3.5L8.5 7.5l3 2-1 2.5C5 12 0 6.5 1 2z" fill="#fff"/></svg>+1 (555) 014 2290</div>
  <div class="social"><span><i></i></span><span><i></i></span><span><i></i></span><span><i></i></span></div>
</div>

<header class="header">
  <div class="brand"><span class="mark"></span><span class="name">Beacon Advisory</span></div>
  <nav class="nav">
    <a class="home"><svg width="18" height="16" viewBox="0 0 18 16"><path d="M9 1L1 8h2.5v7h4v-4h3v4h4V8H17z" fill="#0e3a86"/></svg></a>
    <a>COMPANY</a><a>SERVICES</a><a>SOLUTIONS</a><a>RESOURCES</a><a>CAREER</a><a>CONTACT US</a>
  </nav>
</header>

<section class="hero" role="img" aria-label="Photo of a consultant working on a futuristic transparent touchscreen dashboard">
  <h1>We Will Delivers Highest Level Of Quality<br>Consultants And Services For The<br>Lowest Cost Of Ownership</h1>
  <div class="cta">GET STARTED WITH US</div>

  <div class="card" style="left:84px">
    <div class="tab">CONSULTING</div>
    <div class="icon"><svg width="38" height="38" viewBox="0 0 38 38"><rect x="15" y="3" width="20" height="12" rx="6" fill="none" stroke="#fff" stroke-width="2"/><circle cx="13" cy="16" r="5" fill="#fff"/><path d="M4 34c0-7 4-11 9-11s9 4 9 11z" fill="#fff"/></svg></div>
    <p>Beacon Advisory has certified professional consultants to work with you to help increase the business by providing IT services...</p>
    <span class="more">Read More</span>
  </div>
  <div class="card" style="left:377px">
    <div class="tab">STAFF AUGMENTATION</div>
    <div class="icon"><svg width="40" height="36" viewBox="0 0 40 36"><circle cx="20" cy="8" r="5" fill="#fff"/><circle cx="8" cy="13" r="4" fill="#fff"/><circle cx="32" cy="13" r="4" fill="#fff"/><path d="M12 32c0-8 3-12 8-12s8 4 8 12z" fill="#fff"/><path d="M1 30c0-6 3-9 7-9s6 3 6 9z" fill="#fff"/><path d="M26 30c0-6 2-9 6-9s7 3 7 9z" fill="#fff"/></svg></div>
    <p>For years Beacon Advisory has been offering our customers the ability to augment their existing staff ...</p>
    <span class="more">Read More</span>
  </div>
  <div class="card" style="left:671px">
    <div class="tab">OFFSHORE</div>
    <div class="icon"><svg width="40" height="38" viewBox="0 0 40 38"><g stroke="#fff" stroke-width="1.5" fill="none"><path d="M6 12L20 4 34 12 30 28 10 28z"/><path d="M6 12l14 10 14-10M20 4v18M10 28l10-6 10 6"/></g><g fill="#fff"><circle cx="6" cy="12" r="3"/><circle cx="20" cy="4" r="3"/><circle cx="34" cy="12" r="3"/><circle cx="10" cy="28" r="3"/><circle cx="30" cy="28" r="3"/><circle cx="20" cy="22" r="3.5"/><path d="M14 37c0-5 3-8 6-8s6 3 6 8z"/></g></svg></div>
    <p>Our Offshore development model has a unique distinction of providing efficient software solutions ...</p>
    <span class="more">Read More</span>
  </div>
</section>

<section class="welcome"><h2><span class="dot"></span>WELCOME TO <strong>BEACON ADVISORY</strong></h2></section>
<div class="rule"></div>

<ul class="points">
  <li><svg width="13" height="13" viewBox="0 0 13 13"><circle cx="6.5" cy="6.5" r="6.5" fill="#0e3a86"/><path d="M3.5 6.7l2 2 4-4" stroke="#fff" stroke-width="1.6" fill="none"/></svg>Lorem ipsum dolor sit amet, consectetur adipiscing elit. Nulla fringilla bibendum its orci at convallis. Suspendisse a maximus turpis.</li>
  <li><svg width="13" height="13" viewBox="0 0 13 13"><circle cx="6.5" cy="6.5" r="6.5" fill="#0e3a86"/><path d="M3.5 6.7l2 2 4-4" stroke="#fff" stroke-width="1.6" fill="none"/></svg>Aenean sed blandit lectus, sed hendrerit felis. Etiam a elit eu nisi pulvinar interdudf.</li>
  <li><svg width="13" height="13" viewBox="0 0 13 13"><circle cx="6.5" cy="6.5" r="6.5" fill="#0e3a86"/><path d="M3.5 6.7l2 2 4-4" stroke="#fff" stroke-width="1.6" fill="none"/></svg>Praesent vel leo non enim rutrum lobortis vitae eu ante. Nulla fringilla bibendum eti orci at convallis. Suspendisse a maximus turpis.</li>
  <li><svg width="13" height="13" viewBox="0 0 13 13"><circle cx="6.5" cy="6.5" r="6.5" fill="#0e3a86"/><path d="M3.5 6.7l2 2 4-4" stroke="#fff" stroke-width="1.6" fill="none"/></svg>Nulla fringilla bibendum orci at convallis. Suspendisse a maximus turpis. Praeset vel leo non enim rutrum lobortis vitae eu ante.</li>
  <li><svg width="13" height="13" viewBox="0 0 13 13"><circle cx="6.5" cy="6.5" r="6.5" fill="#0e3a86"/><path d="M3.5 6.7l2 2 4-4" stroke="#fff" stroke-width="1.6" fill="none"/></svg>Praesent vel leo non enim rutrum lobortis vitae eu ante.</li>
</ul>

<div class="tablet" role="img" aria-label="Photo of two hands holding a tablet playing a company video"></div>

<footer class="footer">
  <div class="col links">
    <h3>Quick Links</h3>
    <ul><li>Home</li><li>Company</li><li>Services</li><li>Solutions</li><li>Resources</li><li>Career</li><li>Contact Us</li></ul>
  </div>
  <div class="sep" style="left:226px"></div>
  <div class="col contact">
    <h3>Contact Details</h3>
    <div class="row"><svg width="10" height="13" viewBox="0 0 10 13"><path d="M5 0a5 5 0 00-5 5c0 3.5 5 8 5 8s5-4.5 5-8a5 5 0 00-5-5zm0 7a2 2 0 110-4 2 2 0 010 4z" fill="#fff"/></svg><div><b style="color:#fff">HEAD OFFICE</b><br>42 Harbor Lane<br>Suite 310<br>Riverton, NJ 08077</div></div>
    <div class="row"><svg width="11" height="12" viewBox="0 0 12 13"><path d="M3 1l2 3-1.5 1.5c.7 1.6 2 2.9 3.5 3.5L8.5 7.5l3 2-1 2.5C5 12 0 6.5 1 2z" fill="#fff"/></svg><div>+1 (555) 014 2290</div></div>
    <div class="row"><svg width="12" height="9" viewBox="0 0 12 9"><rect x=".5" y=".5" width="11" height="8" fill="none" stroke="#fff"/><path d="M.5.5L6 5l5.5-4.5" fill="none" stroke="#fff"/></svg><div>info@beaconadvisory.example</div></div>
  </div>
  <div class="sep" style="left:463px"></div>
  <div class="col inquiry">
    <h3>Quick Inquiry</h3>
    <div class="field">Name</div>
    <div class="field">Email</div>
    <div class="field msg">Message</div>
    <div class="btn">Submit</div>
  </div>
  <div class="sep" style="left:727px"></div>
  <div class="f-brand"><span class="mark"></span><span class="name">Beacon Advisory</span></div>
  <div class="f-social"><span style="background:#3b5998"></span><span style="background:#1da1f2"></span><span style="background:#d62b2b"></span><span style="background:#dd4b39"></span></div>
</footer>

<div class="copy">Copyright © 2016 Beacon Advisory Inc. All Rights Reserved.</div>
</body>
</html>
```